Independent Midwife for a positive birth experience needs a vibrant, and elegant business card/logo

I need a business card design with a logo. The logo I would like to be able to use on my website (www.midwifeorlaith.com) next to my name.
Therefore the design of the card and logo should suit the colours and design of the website. The title of the website and company is "Orlaith Denby Marsworth, Midwife" but I'd like to have the business card title to be "Orlaith Denby Marsworth - Independent Midwife" in bold letters, same script font as in my website.

I provide gold standard midwifery services, one-to-one tailored care, continuity of care throughout the entire pregnancy (antenatal care), the birth and after the birth (postnatal care), home birth, water birth, breast-feeding support, and birth preparation workshops. I also am certified and offer complementary therapies: pregnancy reflexology, rebozo techniques for optimal baby positioning.

The design should incorporate similar colours and style as the website and the "Orlaith Denby Marsworth - Independent Midwife" on the card should include the same font as in the title of the website, however, in bold. The front of the card should have a logo, title and contact information (phone number 071592604, email orlaith.marsworth@quillpost.com, website address www.midwifeorlaith.com).
The back of the card to include the services I offer.

The logo: use of colour purple (varying shades), should communicate communicate warmth, kindness, compassion. It should convey that I'm a midwife who believes in fostering a trusting relationship with my clients and to provide them with a positive pregnancy and birth experience.

Target Market(s)

Pregnant women or women who are looking to book a private midwife for better birth experience and outcome

Industry/Entity Type

Baby

Contact Information for Business Card

Name and Title on front side together with contact details
The reverse side should have services/packages offered

Font styles to use
Script
Other font styles liked:
• similar script as in my website for name and title, and easy to read font for the rest of the words

Colors
b768aa
a54599
d2a4cc
ffffff

Requirements
Must have
• same font as title of website, but slightly bolder.
• similar design, colours, patterns as in website.
• Also include a gold accent colour somewhere in the design please.
Nice to have
• perhaps a logo of pregnant belly in profile or newborn baby icon

```html
<!DOCTYPE html>
<html lang="en">
<head>
<meta charset="utf-8">
<title>Orlaith Denby Marsworth – Business Card</title>
<link rel="stylesheet" href="https://fonts.googleapis.com/css2?family=Great+Vibes&family=Open+Sans:wght@300;400&family=Exo+2:wght@400&display=swap">
<style>
  :root {
    --band: #9a1de8;
    --white: #ffffff;
    --lilac: #d2a4cc;
    --gold: #d5a13a;
    --gold-dark: #a8781f;
    --photo-left-a: #3a3a44;
    --photo-left-b: #8d8b98;
    --photo-left-c: #4a3c6a;
    --photo-right-a: #1d1a26;
    --photo-right-b: #5a3d3c;
    --photo-right-c: #2a2236;
  }
  * { margin: 0; padding: 0; box-sizing: border-box; }
  html, body { width: 1200px; height: 333px; overflow: hidden; background: var(--white); }
  .canvas { position: relative; width: 1200px; height: 333px; }
  .card { position: absolute; top: 0; width: 597px; height: 333px; overflow: hidden; color: var(--white); font-family: "Open Sans", sans-serif; }
  .card--front { left: 0; }
  .card--back { left: 603px; }
  .band { position: absolute; top: 0; left: 0; right: 0; height: 47px; background: var(--band); }
  .photo { position: absolute; top: 47px; left: 0; right: 0; bottom: 0; }
  .card--front .photo {
    background:
      radial-gradient(ellipse 40% 60% at 35% 45%, var(--photo-left-b), transparent 70%),
      radial-gradient(ellipse 50% 70% at 80% 100%, var(--photo-left-c), transparent 70%),
      linear-gradient(180deg, var(--photo-left-a), #2c2834);
  }
  .card--back .photo {
    background:
      radial-gradient(ellipse 35% 55% at 45% 45%, var(--photo-right-b), transparent 70%),
      radial-gradient(ellipse 40% 60% at 90% 80%, #4a4058, transparent 70%),
      linear-gradient(180deg, var(--photo-right-a), var(--photo-right-c));
  }
  .email { position: absolute; left: 16px; top: 14px; font-size: 13px; font-weight: 300; }
  .phone { position: absolute; left: 430px; top: 6px; font-family: "Exo 2", sans-serif; font-size: 25px; letter-spacing: 2px; }
  .badge { position: absolute; left: 474px; top: 58px; }
  .web-front { position: absolute; left: 450px; top: 155px; font-size: 11px; font-weight: 300; }
  .logo-mark { position: absolute; left: 156px; top: 140px; width: 42px; height: 42px; border: 1.5px solid var(--white); border-radius: 50%; }
  .logo-name { position: absolute; left: 208px; top: 146px; font-family: "Great Vibes", cursive; font-size: 24px; font-weight: 400; }
  .title { position: absolute; left: 0; right: 0; top: 270px; text-align: center; font-family: "Great Vibes", cursive; font-size: 30px; }
  .back-heading { position: absolute; left: 0; right: 0; top: 11px; text-align: center; font-family: "Great Vibes", cursive; font-size: 22px; font-weight: 400; }
  .services { position: absolute; left: 0; right: 0; top: 77px; text-align: center; font-size: 13px; font-weight: 300; line-height: 24px; }
  .therapies-heading { position: absolute; left: 0; right: 0; top: 208px; text-align: center; font-size: 16px; font-weight: 400; }
  .therapies { position: absolute; left: 0; right: 0; top: 236px; text-align: center; font-size: 13px; font-weight: 300; }
  .sign-mark { position: absolute; left: 16px; top: 290px; width: 32px; height: 32px; border: 1px solid var(--white); border-radius: 50%; }
  .sign-name { position: absolute; left: 55px; top: 306px; font-family: "Great Vibes", cursive; font-size: 13px; }
  .web-back { position: absolute; right: 14px; top: 309px; font-size: 13px; font-weight: 300; }
</style>
</head>
<body>
<div class="canvas">
  <section class="card card--front">
    <div class="band"></div>
    <div class="photo" role="img" aria-label="Soft monochrome photo of a newborn's tiny feet held in a parent's hands"></div>
    <p class="email">orlaith.marsworth@quillpost.com</p>
    <p class="phone">071592604</p>
    <svg class="badge" width="64" height="64" viewBox="0 0 64 64" aria-hidden="true">
      <polygon points="20,40 12,62 22,56 28,63 32,44" fill="var(--gold-dark)"/>
      <polygon points="44,40 52,62 42,56 36,63 32,44" fill="var(--gold-dark)"/>
      <circle cx="32" cy="28" r="26" fill="var(--gold)"/>
      <circle cx="32" cy="28" r="19" fill="none" stroke="var(--white)" stroke-width="1.2"/>
    </svg>
    <p class="web-front">www.midwifeorlaith.com</p>
    <span class="logo-mark" aria-hidden="true"></span>
    <p class="logo-name">Orlaith Denby Marsworth</p>
    <p class="title">Orlaith Denby Marsworth, Independent Midwife</p>
  </section>

  <section class="card card--back">
    <div class="band"></div>
    <div class="photo" role="img" aria-label="Warm dark photo of a newborn's head cradled in a mother's hands"></div>
    <h2 class="back-heading">Midwife Services</h2>
    <p class="services">
      One-to-one tailored care,<br>
      Continuity of care throughout the entire pregnancy (Antenatal Care),<br>
      The birth and after the birth (Postnatal Care),<br>
      Home birth, Water birth, Breast-feeding support,<br>
      Birth preparation workshop.
    </p>
    <h3 class="therapies-heading">Offer Complementary Therapies :</h3>
    <p class="therapies">Pregnancy reflexology, Rebozo techniques for optimal baby positioning.</p>
    <span class="sign-mark" aria-hidden="true"></span>
    <p class="sign-name">Orlaith Denby Marsworth, Independent Midwife</p>
    <p class="web-back">www.midwifeorlaith.com</p>
  </section>
</div>
</body>
</html>
```